Educational Software Company Needs Banner Ads Prompting an Event

We are looking for a series of banner ads (to be used in conjunction with google adwords), pushing people to register for our upcoming road tour, Faculty Trailblazers. Faculty Trailblazers is a series of one-day workshops that offer best practices for individuals in the educational operations industry. To learn more about the event please view the website at: facultytrailblazers.learnwick.example.

Feel free to use any of the language from the website, logo (attached), and the hex colors which are listed in the "must have" section below.

Some language that we have use on other marketing materials:
"We're Hitting the Road!"
Our 2014 road tour is heading to a city near you!
"Invest in Your Success"
"We're Hitting the Road, and Heading Your Way!"
"Faculty Trailblazers - A free, one-day workshop offering lessons for success"
"Seating is Limited - Register Today!"

Supported ad sizes and specs:
250 x 250 square
200 x 200 square
468 x 60 banner
728 x 90 leaderboard
300 x 250 inline rectangle
120 x 600 skyscraper
160 x 600 wide skyscrapper
320 x 50 mobile leaderboard

The call to action for the ad should be to "Register Today!"

Target Market(s)

educational operations professionals, i.e. maintenance directors, energy managers, superintendents, business officers etc...

Industry/Entity Type

Marketing

Requirements
Must have
• event logo and/or event name using event colors; CTA button reading "Register Today!"

Colors:
FT – Red #A63515
R: 166
G: 53
B: 21

FT – Dark Gray #726658
R: 114
G: 102
B: 88

FT – Light Gray #CECECE
R: 206
G: 206
B: 206

FT – Orange #EDA45B
R: 237
G: 164
B: 91
Nice to have
• Consider using list of stops on larger banner ads.

1/14/2014 Seattle, CA
1/16/2014 Phoenix, CA
1/21/2014 Sacramento, CA
1/23/2014 Ontario, CA
2/13/2014 Kilgore, TX
2/11/2014 Coppell, TX
TBD Schaumburg, IL

```html
<!DOCTYPE html>
<html lang="en">
<head>
<meta charset="utf-8">
<title>Faculty Trailblazers – Banner Ad Set</title>
<link href="https://fonts.googleapis.com/css2?family=Anton&family=Open+Sans:wght@400;600;700&display=swap" rel="stylesheet">
<style>
  :root{
    --ft-red:#a63515;
    --ft-dark-gray:#726658;
    --ft-light-gray:#cecece;
    --ft-orange:#eda45b;
    --canvas:#f8f6f2;
    --sky:#b3e3df;
    --hill:#6e8f3c;
    --ink:#222;
    --btn-top:#e88a47;
    --btn-bottom:#b4481a;
  }
  *{box-sizing:border-box;margin:0;padding:0}
  html,body{width:1200px;height:779px;overflow:hidden;background:var(--canvas)}
  body{position:relative;font-family:"Open Sans",Arial,sans-serif;color:var(--ink)}

  .ad{position:absolute;border:1px solid #2a2a2a;overflow:hidden;background:#fff}
  .size-label{position:absolute;font:400 16px "Open Sans",Arial,sans-serif;color:#111;text-align:center}

  .cta{position:absolute;display:flex;align-items:center;justify-content:center;
    background:linear-gradient(var(--btn-top),var(--btn-bottom));border-radius:3px;
    box-shadow:0 2px 2px rgba(0,0,0,.45);color:#fff;font-family:"Anton",Impact,sans-serif;
    letter-spacing:.3px;text-shadow:1px 1px 1px rgba(0,0,0,.6);white-space:nowrap}

  .headline{font-family:"Anton",Impact,sans-serif;color:#fff;text-transform:uppercase;text-align:center;
    text-shadow:1px 1px 2px rgba(0,0,0,.35)}
  .event-name{font-family:"Open Sans",Arial,sans-serif;font-weight:400;color:var(--ft-dark-gray);
    text-transform:uppercase;letter-spacing:.5px;white-space:nowrap}

  .event-mark{position:absolute;display:flex;flex-direction:column;align-items:center;gap:6px;
    color:var(--ft-red);font-weight:700;text-transform:uppercase;text-align:center;line-height:1.1}
  .event-mark .dot{border-radius:50%;background:var(--ft-red)}

  .stops{position:absolute;font-size:9px;line-height:11.2px;color:#111}
  .stops .row{display:flex;justify-content:space-between}
  .stops .tbd{text-align:center}
  .stops.on-red{color:#fff}

  .illustration{position:absolute}
  .road-scene{background:linear-gradient(var(--sky) 0%,var(--sky) 45%,var(--hill) 75%,#5a4a30 100%)}
</style>
</head>
<body>

<!-- 250 x 250 -->
<section class="ad ad-250" style="left:31px;top:31px;width:252px;height:252px;background:linear-gradient(var(--ft-red) 0,var(--ft-red) 45%,#e6e6e6 45%,#fff 100%)">
  <h2 class="headline" style="position:absolute;top:4px;width:100%;font-size:28px;letter-spacing:.5px">Seating is Limited</h2>
  <div class="event-mark" style="left:20px;top:78px;width:210px;font-size:22px">
    <span class="dot" style="width:30px;height:30px;background:#e7a623"></span>
    <span>Faculty<br>Trailblazers</span>
  </div>
  <div class="cta" style="left:59px;top:211px;width:130px;height:33px;font-size:16px">REGISTER TODAY!</div>
</section>
<div class="size-label" style="left:31px;top:304px;width:252px">250 X 250</div>

<!-- 300 x 250 -->
<section class="ad ad-300x250" style="left:335px;top:31px;width:302px;height:252px;background:var(--ft-orange)">
  <div class="illustration road-scene" role="img" aria-label="Illustration of a red station wagon loaded with suitcases driving on a mountain road" style="left:0;top:0;width:140px;height:250px"></div>
  <p style="position:absolute;left:5px;top:5px;font-size:15px;font-weight:600;line-height:25px;color:#111">We're Hitting<br>the Road!</p>
  <div class="stops" style="left:147px;top:12px;width:147px">
    <div class="row"><span>1/14/2014</span><span>Seattle, CA</span></div>
    <div class="row"><span>1/16/2014</span><span>Phoenix, CA</span></div>
    <div class="row"><span>1/21/2014</span><span>Sacramento, CA</span></div>
    <div class="row"><span>1/23/2014</span><span>Ontario, CA</span></div>
    <div class="row"><span>2/13/2014</span><span>Kilgore, TX</span></div>
    <div class="row"><span>2/11/2014</span><span>Coppell, TX</span></div>
    <div class="tbd">TBD Schaumburg, IL</div>
  </div>
  <div class="event-mark" style="left:150px;top:118px;width:145px;font-size:16px">
    <span class="dot" style="width:24px;height:24px;background:#e7a623"></span>
    <span>Faculty<br>Trailblazers</span>
  </div>
  <div class="cta" style="left:165px;top:217px;width:112px;height:30px;font-size:14px">REGISTER TODAY!</div>
</section>
<div class="size-label" style="left:335px;top:304px;width:302px">300 X 250</div>

<!-- 300 x 50 -->
<section class="ad ad-300x50" style="left:31px;top:380px;width:322px;height:52px">
  <div style="position:absolute;left:0;top:0;width:206px;height:26px;background:var(--ft-red);color:#fff;font-size:14px;font-weight:600;line-height:26px;padding-left:7px;white-space:nowrap">We're Hitting the Road!</div>
  <div class="event-name" style="position:absolute;left:7px;top:28px;font-size:16px">Faculty Trailblazers</div>
  <div class="cta" style="left:212px;top:11px;width:104px;height:28px;font-size:12px">REGISTER TODAY!</div>
</section>
<div class="size-label" style="left:31px;top:446px;width:322px">300 X 50</div>

<!-- 468 x 60 -->
<section class="ad ad-468" style="left:31px;top:504px;width:470px;height:62px">
  <div style="position:absolute;left:0;top:0;width:258px;height:60px;background:var(--ft-red);color:#fff;font-size:17px;font-weight:600;line-height:22px;text-align:center;padding-top:8px">Our 2014 road tour is<br>heading to a city near you!</div>
  <div style="position:absolute;left:259px;top:0;width:7px;height:60px;background:var(--ft-dark-gray)"></div>
  <div class="event-name" style="position:absolute;left:274px;top:36px;font-size:16px">Faculty Trailblazers</div>
  <div class="cta" style="left:362px;top:4px;width:102px;height:26px;font-size:12px">REGISTER TODAY!</div>
</section>
<div class="size-label" style="left:31px;top:582px;width:470px">468 X 60</div>

<!-- 200 x 200 -->
<section class="ad ad-200" style="left:559px;top:364px;width:202px;height:252px;background:var(--ft-orange)">
  <div style="position:absolute;left:0;top:0;width:200px;height:102px;background:var(--ft-red);border-bottom:4px solid #fff">
    <h2 class="headline" style="font-size:23px;line-height:30px;margin-top:10px">Invest in your</h2>
    <h2 class="headline" style="font-size:38px;line-height:44px;color:#e8e8e8">Success</h2>
  </div>
  <div class="event-name" style="position:absolute;left:0;width:200px;top:124px;text-align:center;font-size:16px;color:#222">Faculty Trailblazers</div>
  <div class="cta" style="left:37px;top:158px;width:130px;height:34px;font-size:16px">REGISTER TODAY!</div>
</section>
<div class="size-label" style="left:559px;top:582px;width:202px">200 X 200</div>

<!-- 728 x 90 -->
<section class="ad ad-728" style="left:31px;top:631px;width:730px;height:92px">
  <div class="illustration road-scene" role="img" aria-label="Illustration of a red station wagon loaded with suitcases driving through the mountains" style="left:0;top:0;width:170px;height:90px"></div>
  <div style="position:absolute;left:170px;top:0;width:172px;height:90px;background:var(--ft-red)"></div>
  <div class="stops on-red" style="left:180px;top:4px;width:136px">
    <div class="row"><span>1/14/2014</span><span>Seattle, CA</span></div>
    <div class="row"><span>1/16/2014</span><span>Phoenix, CA</span></div>
    <div class="row"><span>1/21/2014</span><span>Sacramento, CA</span></div>
    <div class="row"><span>1/23/2014</span><span>Ontario, CA</span></div>
    <div class="row"><span>2/13/2014</span><span>Kilgore, TX</span></div>
    <div class="row"><span>2/11/2014</span><span>Coppell, TX</span></div>
    <div class="tbd">TBD Schaumburg, IL</div>
  </div>
  <div style="position:absolute;left:342px;top:0;width:8px;height:90px;background:var(--ft-dark-gray)"></div>
  <p style="position:absolute;left:360px;top:4px;font-size:29px;font-weight:600;color:var(--ft-dark-gray);white-space:nowrap">We're Hitting the Road!</p>
  <div class="event-name" style="position:absolute;left:363px;top:62px;font-size:18px">Faculty Trailblazers</div>
  <div class="cta" style="left:594px;top:53px;width:129px;height:34px;font-size:16px">REGISTER TODAY!</div>
</section>
<div class="size-label" style="left:31px;top:738px;width:730px">728 X 90</div>

<!-- 120 x 600 -->
<section class="ad ad-120" style="left:857px;top:31px;width:122px;height:602px;background:linear-gradient(#cfcfcf 250px,#fff 470px)">
  <div style="position:absolute;left:0;top:0;width:120px;height:77px;background:var(--ft-orange);color:#fff;font-size:17px;font-weight:600;line-height:21px;text-align:center;padding-top:18px">Faculty<br>Trailblazers</div>
  <div style="position:absolute;left:0;top:77px;width:120px;height:170px;background:var(--ft-red);color:#fff;font-size:16px;font-weight:600;line-height:21.5px;text-align:center;padding-top:14px">A free,<br>one-day<br>workshop<br>offering<br>lessons for<br>success</div>
  <div class="stops" style="left:3px;top:262px;width:114px;font-size:7px;line-height:9.3px;color:#555">
    <div class="row"><span>1/14/2014</span><span>Seattle, CA</span></div>
    <div class="row"><span>1/16/2014</span><span>Phoenix, CA</span></div>
    <div class="row"><span>1/21/2014</span><span>Sacramento, CA</span></div>
    <div class="row"><span>1/23/2014</span><span>Ontario, CA</span></div>
    <div class="row"><span>2/13/2014</span><span>Kilgore, TX</span></div>
    <div class="row"><span>2/11/2014</span><span>Coppell, TX</span></div>
    <div class="tbd">TBD Schaumburg, IL</div>
  </div>
  <div class="event-mark" style="left:2px;top:405px;width:116px;font-size:14px">
    <span class="dot" style="width:28px;height:28px;background:#e7a623"></span>
    <span>Faculty<br>Trailblazers</span>
  </div>
  <div class="cta" style="left:4px;top:551px;width:112px;height:30px;font-size:13px">REGISTER TODAY!</div>
</section>
<div class="size-label" style="left:857px;top:656px;width:122px">120 X 600</div>

<!-- 160 x 600 -->
<section class="ad ad-160" style="left:1008px;top:31px;width:162px;height:602px;background:linear-gradient(#f7c79a 160px,#fff 330px)">
  <div style="position:absolute;left:0;top:0;width:160px;height:159px;background:var(--ft-red);color:#fff;font-size:20px;font-weight:600;line-height:25.5px;text-align:center;padding-top:10px">We're<br>Hitting the<br>Road, and<br>Heading<br>Your Way!</div>
  <div class="stops" style="left:5px;top:180px;width:150px">
    <div class="row"><span>1/14/2014</span><span>Seattle, CA</span></div>
    <div class="row"><span>1/16/2014</span><span>Phoenix, CA</span></div>
    <div class="row"><span>1/21/2014</span><span>Sacramento, CA</span></div>
    <div class="row"><span>1/23/2014</span><span>Ontario, CA</span></div>
    <div class="row"><span>2/13/2014</span><span>Kilgore, TX</span></div>
    <div class="row"><span>2/11/2014</span><span>Coppell, TX</span></div>
    <div class="tbd">TBD Schaumburg, IL</div>
  </div>
  <div class="event-mark" style="left:5px;top:345px;width:150px;font-size:20px">
    <span class="dot" style="width:40px;height:40px;background:#e7a623"></span>
    <span>Faculty<br>Trailblazers</span>
  </div>
  <div class="cta" style="left:8px;top:551px;width:145px;height:38px;font-size:17px">REGISTER TODAY!</div>
</section>
<div class="size-label" style="left:1008px;top:656px;width:162px">160 X 600</div>

</body>
</html>
```